IT Consulting Site Revamping for Varnel

I've put a skeleton together on my website, but realize I need some help (it's http://pilot.varnel-example.ca).
I've pulled together tidbits from other websites, but really need my site to be cleaned up, and really spruced up.
I primarily focus on the IT needs of small to medium size businesses, taking care of everything from their servers and networks down to their workstations.
I also want a page listing the vendors (and logos) that I work with including Brontisoft, QZWare, Pelvar, Fusk, TQ, ZRL, WUBE, Morva, Trelagate.
There should also be a simple form to get a quote that will email me.
The final design should communicate strength and reliability.
I would like this to be a fully functional website, that I can upload to Plimba Pages, with the same sort of pages that are existing on http://pilot.varnel-example.ca
Updates
Hey everyone,
Hi everyone,
Reason: Hi all,
There are some designers that would like to submit some new designs, so I'm extending the deadline.
Thanks,
Target Market(s)
Small to medium size business owners. This will primarily be males who work in the oil and gas industry.
Industry/Entity Type
Consulting
Look and feel
Each slider illustrates characteristics of the customer's brand and the style your logo design should communicate.

```html
<!DOCTYPE html>
<html lang="en">
<head>
<meta charset="utf-8">
<title>Varnel – Small Business IT Services</title>
<link href="https://fonts.googleapis.com/css2?family=Open+Sans:ital,wght@0,400;0,600;0,700;1,400&family=Arimo:wght@400;700&display=swap" rel="stylesheet">
<style>
:root{
  --brand:#1b6fb0;
  --brand-dark:#0d3f86;
  --navy:#0b3a8a;
  --nav-top:#6aa9d6;
  --nav-bottom:#1f66a6;
  --band:#ececec;
  --text:#2b2b2b;
  --muted:#555;
  --heading:#444;
  --link:#1a4a9a;
  --cta:#1fb4e4;
  --field:#9aa4ad;
  --social:#3b78b8;
}
*{box-sizing:border-box;margin:0;padding:0}
html,body{width:1200px;height:966px;overflow:hidden;background:#fff}
body{position:relative;font-family:"Open Sans",sans-serif;color:var(--text)}
.wrap{position:absolute;left:171px;width:850px}

.brand{display:flex;align-items:center;gap:12px}
.brand-dot{width:62px;height:62px;border-radius:50%;background:var(--brand)}
.brand-name{font-family:"Open Sans",sans-serif;font-weight:600;color:var(--brand);font-size:44px;letter-spacing:-1px}
.header-brand{top:30px}

.social{display:flex;gap:5px}
.social span{width:18px;height:18px;border-radius:3px;background:var(--social)}
.header-social{position:absolute;top:20px;right:179px}

.search{position:absolute;top:73px;right:179px;display:flex;height:25px}
.search input{width:156px;border:1px solid #cfd5da;border-right:0;border-radius:3px 0 0 3px;padding:0 10px;font:12px "Open Sans",sans-serif;color:#aaa;box-shadow:inset 1px 1px 3px #ddd}
.search button{width:24px;border:0;border-radius:0 3px 3px 0;background:linear-gradient(#4a86c0,#1a5796);color:#fff;font:11px "Open Sans",sans-serif}

.nav{top:126px;height:41px;display:flex;border-radius:3px;overflow:hidden;background:linear-gradient(var(--nav-top),var(--nav-bottom));border:1px solid #2a6aa5}
.nav a{display:flex;align-items:center;justify-content:center;color:#fff;text-decoration:none;font-size:14px;border-right:1px solid #1b5a94;box-shadow:inset 1px 0 0 rgba(255,255,255,.25)}
.nav a:last-child{border-right:0}
.nav .current{font-weight:700;font-family:"Arimo",sans-serif;font-size:15px}

.hero{top:190px;height:219px;background:linear-gradient(90deg,#f3f6f9 0%,#e3ebf2 35%,#a9c7e2 58%,#2f82c6 78%,#1a6db4 100%);overflow:hidden}
.hero-photo{position:absolute;right:0;top:0;width:340px;height:219px;background:linear-gradient(90deg,rgba(40,120,190,0),#1e5d95 55%,#243240)}
.hero h1{position:absolute;left:43px;top:64px;font-family:"Arimo",sans-serif;font-weight:700;color:var(--navy);line-height:1}
.hero h1 .big{display:block;font-size:30px}
.hero h1 .small{display:block;font-size:19px;margin-top:0}
.hero .tagline{position:absolute;left:43px;top:125px;font-style:italic;color:var(--navy);font-size:17px}
.hero .cta{position:absolute;left:349px;top:162px;width:102px;height:37px;border-radius:4px;background:linear-gradient(#2a9ccb,#125d86);color:#fff;font-size:16px;display:flex;align-items:center;justify-content:center;box-shadow:0 1px 2px rgba(0,0,0,.4)}

.vendors{position:absolute;top:409px;left:0;width:1200px;height:94px;background:var(--band)}
.vendors ul{position:absolute;left:171px;width:850px;top:0;height:94px;list-style:none;display:flex;justify-content:space-between;align-items:center}
.vendors li{font-family:"Arimo",sans-serif;font-weight:700;font-size:18px;color:#7a7a7a}

.about{top:537px;width:555px}
.about h2{font-family:"Arimo",sans-serif;font-size:18px;color:var(--brand);margin-bottom:6px}
.about p{font-family:"Arimo",sans-serif;font-size:11.4px;line-height:18px;color:var(--text)}
.about .more{display:block;text-align:right;font-family:"Arimo",sans-serif;font-size:11.4px;color:var(--link);margin-top:10px;text-decoration:none}

.contact{position:absolute;left:793px;top:539px;width:170px}
.contact h2{font-family:"Arimo",sans-serif;font-size:18px;color:var(--heading);margin-bottom:12px}
.contact label{display:flex;align-items:center;justify-content:space-between;font-size:11.5px;color:var(--heading);margin-bottom:7px}
.contact input{width:111px;height:20px;border:1px solid var(--field);border-radius:3px;box-shadow:inset 1px 1px 2px #ccc}
.contact .msg{display:block;font-size:11.5px;color:var(--heading);margin:12px 0 5px 2px}
.contact textarea{display:block;width:157px;height:99px;margin-left:2px;border:1px solid var(--field);border-radius:2px;resize:none}
.contact button{display:block;margin:9px 0 0 84px;width:75px;height:27px;border:0;border-radius:3px;background:linear-gradient(var(--cta),#0f8ec3);color:#fff;font:14px "Open Sans",sans-serif}

.footer-nav{top:848px;display:flex;gap:15px;font-size:10px;color:#333}
.footer-follow{position:absolute;top:848px;right:179px;font-size:10px;color:#333}
.footer-follow .social{margin-top:6px}
.footer-brand{position:absolute;left:171px;top:895px;display:flex;align-items:center;gap:10px}
.footer-brand .brand-dot{width:50px;height:50px}
.footer-brand .brand-name{font-size:34px}
.footer-brand small{font-size:10px;color:#444;margin-left:4px;align-self:flex-end;margin-bottom:6px}
</style>
</head>
<body>

<header>
  <div class="wrap brand header-brand">
    <span class="brand-dot"></span><span class="brand-name">Varnel</span>
  </div>
  <div class="social header-social" aria-label="Social links"><span></span><span></span><span></span><span></span><span></span><span></span></div>
  <form class="search"><input value="search.."><button type="button">go</button></form>
</header>

<nav class="wrap nav">
  <a class="current" style="width:138px">Home</a>
  <a style="width:187px">Our Services</a>
  <a style="width:167px">About us</a>
  <a style="width:188px">Our Products</a>
  <a style="width:170px">Contact us</a>
</nav>

<section class="wrap hero">
  <div class="hero-photo" role="img" aria-label="Photo of a businessman holding an open laptop"></div>
  <h1><span class="big">Small Business</span><span class="small">Information Technology Services</span></h1>
  <p class="tagline">Easy, Affordable and Reliable.</p>
  <a class="cta">read more</a>
</section>

<section class="vendors" aria-label="Vendors">
  <ul><li>Brontisoft</li><li>TQ</li><li>Pelvar</li><li>ZRL</li><li>Morva</li><li>Trelagate</li><li>Fusk</li><li>QZWare</li><li>WUBE</li></ul>
</section>

<section class="wrap about">
  <h2>About Varnel</h2>
  <p>Varnel Solutions is a computer solutions provider and IT consulting firm that supports a wide variety of local small businesses in the Calgary area primarily. Our company also provides IT services to businesses throughout Alberta on special projects.</p>
  <p>Varnel has been trusted for over the last 7 years by small business companies like yours. Whether you are looking for an ongoing computer support company, looking to outsource your small business computer work, or just looking for a computer company to help you solve a computer problem, Varnel is your right choice.</p>
  <p>We have a diversity of small business support solutions. We provide in office, over the phone, remote or drop-off computer technical support services to small business.</p>
  <p>Our computer technicians and network professionals understand that your business operations hinge on computer and network availability. Regardless if your business has one or many business locations, our preventive and ongoing business support solutions can help you keep all your computer systems running smoothly.</p>
  <p>Our computer business support services deliver unmatched reliability and expertise in computer networking, remote</p>
  <a class="more">Read more &gt;&gt;</a>
</section>

<form class="contact">
  <h2>Contact us</h2>
  <label>Name: <input></label>
  <label>Email: <input></label>
  <span class="msg">Message:</span>
  <textarea></textarea>
  <button type="button">submit</button>
</form>

<footer>
  <div class="wrap footer-nav"><span>Home</span><span>Our Services</span><span>About us</span><span>Our Products</span><span>Contact us</span></div>
  <div class="footer-follow">Follow us
    <div class="social"><span></span><span></span><span></span><span></span><span></span><span></span></div>
  </div>
  <div class="footer-brand">
    <span class="brand-dot"></span><span class="brand-name">Varnel</span><small>2012. All rights reserved</small>
  </div>
</footer>

</body>
</html>
```